Wordpress Design for crazy innovation company

I need an wordpress design for a hosted wordpress site. I have a new logo for the company, but no corporate design guide/color palette etc.

The main features of the website is a blog and a reference section.

Reference section structure:
About us
How to (with subpages)
Entrepreneurship (with subpages)
Links

Blog items
I will use keywords and comments, categories and tags.
Images will be used and should be clickable to see larger picture.

See qorvalent.com for some sample content (in norwegian).

Nature of business:
- Q7 Ventrix is a small innovative company guiding entrepreneurs and invests in tech startups (business angel) software and electronics. And in addition have a few crazy projects building prototypes for new electronics, software and apps.
- my background: software, hardware, marketing, sales

Inspiration websites:
http://launchersbrightpatternhall.com
http://quillbyte.com
http://plumagrove.net/item/brisket/full_screen_preview/31746
http://www.tarnwick.com/themes/preview/?item=lumen
http://dovemarble.com
http://www.gravelbarnworks.com

Favourite colors:
- pink
- orange
Updates

Instead of creating a bunch of custom css/html, i would like the final design to be based on the http://www.brellaforms.com/2012/06/easel/ theme.

Target Market(s)

entrepreneurs & investors

Industry/Entity Type

Software

Requirements
Must have
• Deliverables:
- Photoshop PSD/Illustrator AI files
- CSS/HTML suited for wordpress hosted

```html
<!DOCTYPE html>
<html lang="en">
<head>
<meta charset="utf-8">
<title>Q7 Ventrix</title>
<link href="https://fonts.googleapis.com/css2?family=Ropa+Sans&display=swap" rel="stylesheet">
<style>
:root{
  --page:#f7f7f8;
  --ink:#333;
  --muted:#606060;
  --magenta:#c8178f;
  --magenta-light:#e04bb0;
  --orange:#f8ae14;
  --brand-blue:#3a9ad9;
  --line:#b9b9b9;
  --footer:#dcdcdd;
}
*{box-sizing:border-box;margin:0;padding:0}
html,body{width:813px;height:1200px;overflow:hidden}
body{background:var(--page);font-family:"Ropa Sans",sans-serif;color:var(--ink);position:relative}
.abs{position:absolute}
.brand{left:56px;top:12px;display:flex;align-items:center;gap:10px;font-family:"Ropa Sans",sans-serif;font-size:40px;line-height:46px;color:#1e1e1e;text-transform:uppercase}
.brand-mark{width:46px;height:46px;background:var(--brand-blue)}
.search{left:599px;top:12px;width:151px;height:22px;border:1px solid #aaa;border-radius:4px;background:#fff;font-size:9px;color:#666;padding:5px 8px}
.search svg{position:absolute;right:6px;top:5px}
.tel{right:63px;top:45px;font-size:17px;color:#222}
.nav{left:0;top:77px;width:813px;height:30px;background:linear-gradient(var(--magenta-light),var(--magenta));display:flex;align-items:center;padding-left:58px}
.nav a{color:#fff;text-decoration:none;font-size:12.5px;margin-right:33px}
.nav a.current{background:var(--orange);color:#333;border-radius:4px;padding:3px 13px;margin-right:18px}
.hero{left:56px;top:108px;width:696px;height:242px;background:linear-gradient(100deg,#e6e6e6 0%,#8d8d8d 50%,#3a3a3a 85%,#1c1c1c 100%)}
.dots{left:61px;top:319px;width:61px;height:21px;background:#fff;display:flex;gap:5px;align-items:center;justify-content:center}
.dots i{width:9px;height:9px;border-radius:50%;background:#444}
.dots i:first-child{background:var(--magenta)}
h2{font-weight:400;font-size:16px;color:#222}
h3{font-weight:400;font-size:17px;color:#333}
p{font-size:8.6px;line-height:12.2px;color:var(--muted)}
p+p{margin-top:12px}
.products-title{left:56px;top:364px}
.product-img{left:56px;top:394px;width:129px;height:144px;border:1px solid #444;background:linear-gradient(160deg,#2f7fc9,#7fb7e0 60%,#5f9e3c)}
.product-text{left:202px;top:391px;width:550px}
.product-text h3{margin-bottom:9px}
.about{left:58px;top:558px;width:476px;height:222px;border:1px solid var(--line);background:linear-gradient(#fff 60%,#eee);padding:18px 26px}
.about h2{font-size:17px;margin-bottom:11px}
.about p{font-size:8.2px}
.about p+p{margin-top:20px}
.side{left:550px;width:200px;height:70px;background:linear-gradient(#ececed,#dedee0);padding:9px 20px}
.side h2{font-size:16px;margin-bottom:6px}
.side p{font-size:8px;line-height:12px}
.tabs{left:57px;top:804px;display:flex;gap:2px}
.tab{width:117px;height:33px;border-radius:5px 5px 0 0;background:var(--orange);color:#333;font-size:13px;text-align:center;padding-top:8px}
.tab.active{background:var(--magenta);color:#fff}
.tab-panel{left:57px;top:837px;width:695px;height:174px;border:1px solid var(--line);background:linear-gradient(#fff 60%,#efefef)}
.tab-img{left:70px;top:853px;width:156px;height:141px;border:2px solid #ddd;background:radial-gradient(circle at 45% 60%,#c9c9c9,#6d6d6d 70%,#4a4a4a)}
.tab-text{left:241px;top:852px;width:500px}
.tab-text h3{margin-bottom:8px}
.footer{left:0;top:1035px;width:813px;height:135px;background:var(--footer)}
.links-title{left:57px;top:1044px;font-size:16px}
.links{top:1074px;font-size:9px;line-height:16.3px;color:#222}
.divider{left:585px;top:1044px;width:1px;height:114px;background:#555}
.feed{left:601px;top:1044px;width:150px}
.feed h2{margin-bottom:8px}
.feed p{font-size:7.8px;color:#222}
.feed small{font-size:7.6px;color:#555}
.copy{left:0;top:1170px;width:813px;height:30px;background:#fafafa;border-top:1px solid #bbb;border-bottom:1px solid #888;font-size:8.5px;padding:9px 57px;color:#111}
</style>
</head>
<body>
<header>
  <div class="abs brand"><span class="brand-mark"></span>Q7 Ventrix</div>
  <div class="abs search">Search
    <svg width="10" height="10" viewBox="0 0 10 10"><circle cx="6" cy="4" r="3" fill="none" stroke="#1a6fb5" stroke-width="1.3"/><line x1="4" y1="6" x2="1" y2="9" stroke="#1a6fb5" stroke-width="1.5"/></svg>
  </div>
  <div class="abs tel">Tel: (XXX) XXX XXXX</div>
</header>
<nav class="abs nav">
  <a class="current">Home</a><a>About Us</a><a>Entrepreneurs</a><a>Investors</a><a>Products</a><a>Testimonials</a><a>Blog</a><a>Support</a><a>Contact</a>
</nav>
<div class="abs hero" role="img" aria-label="Photo of a businessman's hand writing with a pen, world map in the background"></div>
<div class="abs dots"><i></i><i></i><i></i><i></i></div>

<h2 class="abs products-title">Our Products</h2>
<div class="abs product-img" role="img" aria-label="Hand placing white blocks against a blue sky and green field"></div>
<div class="abs product-text">
  <h3>Lorem Ipsum is simply dummy text</h3>
  <p>Printing and typesetting industry. Lorem Ipsum has been the industry's standard dummy text ever since the 1500s, when an unknown printer took a galley of type and scrambled it to make a type specimen book. It has survived not only five centuries, but also the leap into electronic typesetting, remaining essentially unchanged.</p>
  <p>It was popularised in the 1960s with the release of Quillset sheets containing Lorem Ipsum passages, and more recently with desktop publishing software like Orvane PageSetter including versions of Lorem Ipsum.</p>
  <p>It was popularised in the 1960s with the release of Quillset sheets containing Lorem Ipsum passages, and more recently with desktop publishing software like Orvane PageSetter including versions of Lorem Ipsum.</p>
</div>

<section class="abs about">
  <h2>About Us</h2>
  <p>Lorem Ipsum is simply dummy text of the printing and typesetting industry. Lorem Ipsum has been the industry's standard dummy text ever since the 1500s, when an unknown printer took a galley of type and scrambled it to make a type specimen book. It has survived not only five centuries, but also the leap into electronic typesetting, remaining essentially unchanged. It was popularised in the 1960s with the release of Quillset sheets containing Lorem Ipsum passages, and more recently with desktop publishing software like Orvane PageSetter including versions of Lorem Ipsum.</p>
  <p>Lorem Ipsum is simply dummy text of the printing and typesetting industry. Lorem Ipsum has been the industry's standard dummy text ever since the 1500s, when an unknown printer took a galley of type and scrambled it to make a type specimen book. It has survived not only five centuries, but also the leap into electronic typesetting, remaining essentially unchanged. It was popularised in the 1960s with the release of Quillset sheets containing Lorem Ipsum passages, and more recently with desktop publishing software like Orvane PageSetter including versions of Lorem Ipsum.</p>
</section>
<aside>
  <div class="abs side" style="top:558px"><h2>Archives</h2><p>Lorem Ipsum is simply dummy text of the printing and typesetting industry.</p></div>
  <div class="abs side" style="top:634px"><h2>Popular Posts</h2><p>Lorem Ipsum is simply dummy text of the printing and typesetting industry.</p></div>
  <div class="abs side" style="top:710px"><h2>Categories</h2><p>Lorem Ipsum is simply dummy text of the printing and typesetting industry.</p></div>
</aside>

<div class="abs tabs"><div class="tab active">Company Overview</div><div class="tab">Entrepreneurs</div><div class="tab">Investors</div></div>
<div class="abs tab-panel"></div>
<div class="abs tab-img" role="img" aria-label="Photo of a person touching a diagram with words thinking, goal and creative"></div>
<div class="abs tab-text">
  <h3>Lorem Ipsum is simply dummy text</h3>
  <p>Printing and typesetting industry. Lorem Ipsum has been the industry's standard dummy text ever since the 1500s, when an unknown printer took a galley of type and scrambled it to make a type specimen book. It has survived not only five centuries, but also the leap into electronic typesetting, remaining essentially unchanged.</p>
  <p>It was popularised in the 1960s with the release of Quillset sheets containing Lorem Ipsum passages, and more recently with desktop publishing software like Orvane PageSetter including versions of Lorem Ipsum.</p>
  <p>It was popularised in the 1960s with the release of Quillset sheets containing Lorem Ipsum passages, and more recently with desktop publishing software like Orvane PageSetter including versions of Lorem Ipsum.</p>
</div>

<footer>
  <div class="abs footer"></div>
  <h2 class="abs links-title">Quick Links</h2>
  <div class="abs links" style="left:59px">Home<br>About Us<br>Entrepreneurs<br>Investors</div>
  <div class="abs links" style="left:174px">Blog<br>Order Now<br>Specials<br>Support</div>
  <div class="abs links" style="left:289px">Contact Us<br>Products<br>Testimonials<br>Terms &amp; Conditions</div>
  <div class="abs links" style="left:418px">Terms Of Use<br>Contact Us<br>Stay Connected</div>
  <div class="abs divider"></div>
  <div class="abs feed">
    <h2>Chirpline Feed</h2>
    <p>Lorem Ipsum is simply dummy text of the printing and typesetting industry. Lorem Ipsum has been the industry's standard dummy text ever since the 1500s, when an unknown printer.</p>
    <small>1 Day Ago</small>
  </div>
  <div class="abs copy">Copyright © 2012. All Rights Reserved.</div>
</footer>
</body>
</html>
```